Website redesign for a technology and engineering company

We'd like to redesign our website which can be found on quorvane.co.nz
!! Please find the designers brief as an uploaded file with all details in there!!
The main purpose for redesign is:
>change of services offered
>old website not very user friendly to maintain or update
Key requirements:
>visually appealing
>easy to navigate
>simple and easy to read
>responsive
>mobile device compatibility
>integrating best SEO practice
All the details are in the attached designer brief document.

```html
<!DOCTYPE html>
<html lang="en">
<head>
<meta charset="utf-8">
<title>Quorvane — Website Design</title>
<link href="https://fonts.googleapis.com/css2?family=Michroma&family=Roboto:wght@400;500;700&display=swap" rel="stylesheet">
<style>
:root{
  --board:#a3a3a3;
  --white:#ffffff;
  --ink:#111111;
  --text:#555555;
  --muted:#777777;
  --dark:#1b1c1f;
  --field:#f0f0f0;
  --line:#dddddd;
}
*{margin:0;padding:0;box-sizing:border-box}
html,body{width:1200px;height:2265px;overflow:hidden;background:var(--board)}
body{font-family:'Roboto',sans-serif;color:var(--ink)}
.board{position:absolute;left:0;top:0;width:1365px;height:2576px;transform:scale(0.87912);transform-origin:0 0}
.abs{position:absolute}
.screen{position:absolute;background:var(--white);overflow:hidden}
.desktop{left:93px;top:98px;width:850px;height:2378px}
.mobile{left:1060px;top:98px;width:212px;height:2102px}
.display{font-family:'Michroma',sans-serif;font-weight:400;letter-spacing:2px;color:var(--ink)}
.center{text-align:center}
.brand{font-family:'Roboto',sans-serif;font-weight:500;color:var(--ink);display:flex;align-items:center;gap:6px}
.brand .dot{width:12px;height:12px;border-radius:50%;background:var(--ink)}
.photo{position:absolute}
.hero-photo{background:linear-gradient(180deg,#d7dbe2 0%,#b9bfcc 30%,#6d7892 55%,#4d5670 72%,#7d7450 88%,#8f7f4e 100%)}
.sea-photo{background:linear-gradient(180deg,#a9c6ea 0%,#dfe8f2 30%,#3e4a3a 40%,#3b6ea8 55%,#2f5e96 70%,#c4282e 85%,#a51e25 100%)}
.alpine{background:linear-gradient(180deg,#1f4fa3 0%,#2d5cae 45%,#6e6c6a 70%,#3a3836 100%)}
.hub{background:linear-gradient(180deg,#5b8bd0 0%,#3f6ea0 40%,#a6aaa9 65%,#3e4a30 100%)}
.rail{background:linear-gradient(180deg,#bcd3ee 0%,#8fa6b8 30%,#6b5a48 60%,#4a3528 100%)}
.person{background:radial-gradient(circle at 50% 35%,#6f86b0 0%,#4a5a6e 50%,#6a6a62 75%,#d06a2a 100%)}
.nav a{position:absolute;font-size:11px;font-weight:500;color:var(--ink);text-decoration:none}
.pill{position:absolute;border:1.5px solid var(--ink);border-radius:20px;font-weight:700;text-align:center;text-transform:uppercase;color:var(--ink);background:var(--white)}
.pill.active{background:var(--ink);color:var(--white)}
.service-list{list-style:none;position:absolute}
.service-list li{display:flex;align-items:center;color:var(--muted)}
.service-list .mark{display:inline-block;border:1.5px solid var(--ink);border-radius:50%;margin-right:10px}
.card{position:absolute;color:var(--white);display:flex;flex-direction:column;justify-content:flex-end;text-align:center;font-weight:700}
.card.dark{background:var(--dark);justify-content:center;font-weight:400}
.card .t{font-weight:700}
.badge{position:absolute;border-radius:50%;background:var(--ink);color:var(--white);text-align:center;display:flex;flex-direction:column;justify-content:center;border:3px solid var(--white)}
.para{position:absolute;color:var(--muted)}
.contact{position:absolute;left:0;background:linear-gradient(180deg,#2a2b2e 0%,#1a1b1d 60%,#121214 100%)}
.field{position:absolute;background:var(--white);border-radius:2px;color:#999}
.ghost{position:absolute;border:1.5px solid var(--white);border-radius:20px;color:var(--white);font-weight:700;text-align:center}
.rule{position:absolute;height:1px;background:var(--line)}
.footnav{position:absolute;font-weight:700;color:var(--ink);text-align:center}
.copy{position:absolute;color:#444;text-align:center}
.copy u{color:var(--ink)}
</style>
</head>
<body>
<div class="board">

<!-- DESKTOP -->
<section class="screen desktop">
  <div class="photo hero-photo" style="left:0;top:0;width:850px;height:520px" role="img" aria-label="Survey station on an alpine ridge above a braided river valley"></div>
  <div class="abs brand" style="left:102px;top:30px;font-size:22px"><span class="dot"></span>Quorvane</div>
  <nav class="nav">
    <a style="left:270px;top:34px">Home</a>
    <a style="left:315px;top:34px">What We Do</a>
    <a style="left:388px;top:34px">Our Projects</a>
    <a style="left:462px;top:34px">About Us</a>
    <a style="left:522px;top:34px">Contact Us</a>
  </nav>
  <div class="pill" style="left:640px;top:25px;width:109px;height:31px;line-height:28px;font-size:9px;background:transparent">Get in touch</div>
  <h1 class="abs display center" style="left:0;top:140px;width:850px;font-size:33px;line-height:42px;letter-spacing:3px">PRECISION. EFFICIENCY.<br>CLARITY.</h1>
  <div class="abs" style="left:783px;top:202px;width:7px;height:7px;border-radius:50%;background:var(--ink)"></div>
  <div class="abs" style="left:783px;top:213px;width:7px;height:7px;border-radius:50%;background:#d8d8d8"></div>
  <div class="abs" style="left:783px;top:224px;width:7px;height:7px;border-radius:50%;background:#d8d8d8"></div>
  <div class="abs" style="left:783px;top:235px;width:7px;height:7px;border-radius:50%;background:#d8d8d8"></div>
  <svg class="abs" style="left:0;top:400px" width="850" height="130" viewBox="0 0 850 130">
    <path d="M0,40 C150,95 300,112 420,98 C560,80 700,48 850,62 L850,130 L0,130Z" fill="#fff"/>
    <path d="M0,40 C150,95 300,112 420,98 C560,80 700,48 850,62 L850,70 C700,58 560,98 420,115 C300,126 150,112 0,46Z" fill="#000"/>
  </svg>

  <h2 class="abs display center" style="left:0;top:564px;width:850px;font-size:23px">WHAT WE DO</h2>
  <div class="pill active" style="left:135px;top:610px;width:184px;height:32px;line-height:29px;font-size:10px">Fieldwork Solutions</div>
  <div class="pill" style="left:333px;top:610px;width:184px;height:32px;line-height:29px;font-size:10px">Positioning and Monitoring</div>
  <div class="pill" style="left:532px;top:610px;width:184px;height:32px;line-height:29px;font-size:10px">Design and Prototyping</div>

  <div class="photo sea-photo" style="left:101px;top:685px;width:323px;height:221px;border-radius:4px" role="img" aria-label="Red inflatable boat bow heading across the sea toward a rocky coast"></div>
  <h3 class="abs" style="left:477px;top:700px;font-size:20px;font-weight:700;letter-spacing:1px">FIELDWORK SOLUTIONS</h3>
  <ul class="service-list" style="left:477px;top:740px;font-size:10px">
    <li style="height:19.3px"><span class="mark" style="width:10px;height:6px"></span>Efficient product rollouts</li>
    <li style="height:19.3px"><span class="mark" style="width:10px;height:6px"></span>Equipment Installation &amp; Maintenance</li>
    <li style="height:19.3px"><span class="mark" style="width:10px;height:6px"></span>Surveying Techniques</li>
    <li style="height:19.3px"><span class="mark" style="width:10px;height:6px"></span>Precision GNSS instrumentation</li>
    <li style="height:19.3px"><span class="mark" style="width:10px;height:6px"></span>Seismic Instrumentation</li>
    <li style="height:19.3px"><span class="mark" style="width:10px;height:6px"></span>IOT Sensors</li>
    <li style="height:19.3px"><span class="mark" style="width:10px;height:6px"></span>Reliable Communications Systems</li>
    <li style="height:19.3px"><span class="mark" style="width:10px;height:6px"></span>Environmental sensors</li>
  </ul>

  <h2 class="abs display center" style="left:0;top:973px;width:850px;font-size:23px">CASE STUDIES</h2>
  <div class="card" style="left:0;top:1029px;width:204px;height:256px">
    <div class="photo alpine" style="inset:0" role="img" aria-label="Solar-powered camera mast on an alpine rock ridge"></div>
    <div class="t" style="position:relative;font-size:11px;padding:0 16px 22px">Remote camera installation in Alpine Environment</div>
  </div>
  <div class="card" style="left:215px;top:1029px;width:204px;height:256px">
    <div class="photo hub" style="inset:0" role="img" aria-label="Technician on a ladder fitting a dish above an equipment hut"></div>
    <div class="t" style="position:relative;font-size:11px;padding:0 16px 28px">Communications hub upgrade</div>
  </div>
  <div class="card dark" style="left:431px;top:1029px;width:204px;height:256px;padding:0 12px">
    <div class="t" style="font-size:11px;line-height:16px;margin-bottom:12px">GNSS CORS station upgrade<br>and survey</div>
    <p style="font-size:8.5px;line-height:16px">Upgrade and reference mark survey of GNSS Continuously Operating Reference Stations (CORS) for the NZGA positioning network. This project enhanced the accuracy and reliability of the NZGA positioning network, crucial for a wide range of applications including land surveying, construction, and geospatial research.</p>
  </div>
  <div class="card" style="left:646px;top:1029px;width:204px;height:256px">
    <div class="photo rail" style="inset:0" role="img" aria-label="Twisted rail tracks and damaged bridge after a flood"></div>
    <div class="t" style="position:relative;font-size:11px;padding:0 16px 22px">Aerial survey for Post-Disaster Recovery</div>
  </div>

  <div class="photo person" style="left:114px;top:1352px;width:266px;height:266px;border-radius:50%" role="img" aria-label="Team member in orange hi-vis on a mountain summit"></div>
  <div class="badge" style="left:303px;top:1524px;width:84px;height:84px;font-size:9px;line-height:14px"><b style="font-size:14px;line-height:18px">15+</b>Years of<br>Experience</div>
  <h2 class="abs display" style="left:448px;top:1408px;font-size:23px">ABOUT US</h2>
  <p class="para" style="left:448px;top:1450px;width:305px;font-size:9.5px;line-height:17px">Welcome to Quorvane, your reliable partner in delivering innovative solutions. Our team of skilled professionals is committed to excellence, ensuring every project is handled with precision, efficiency, and integrity.</p>
  <p class="para" style="left:448px;top:1512px;width:305px;font-size:9.5px;line-height:17px">We solve problems in the field, build robust infrastructure, and deliver accurate data to our clients. Let us help you achieve your goals with our tailored, sustainable solutions and exceptional service.</p>

  <div class="contact" style="top:1677px;width:850px;height:400px" role="img" aria-label="Dark mountain landscape at dusk"></div>
  <h2 class="abs display center" style="left:0;top:1720px;width:850px;font-size:23px;color:var(--white)">CONTACT US</h2>
  <div class="field" style="left:131px;top:1771px;width:285px;height:33px;font-size:9px;padding:12px">Name</div>
  <div class="field" style="left:131px;top:1815px;width:285px;height:33px;font-size:9px;padding:12px">Email Address</div>
  <div class="field" style="left:131px;top:1858px;width:285px;height:33px;font-size:9px;padding:12px">Phone Number</div>
  <div class="field" style="left:431px;top:1770px;width:288px;height:122px;font-size:9px;padding:12px">Message</div>
  <div class="ghost" style="left:357px;top:1927px;width:136px;height:33px;line-height:30px;font-size:11px">SUBMIT NOW &#10140;</div>
  <svg class="abs" style="left:0;top:1980px" width="850" height="100" viewBox="0 0 850 100">
    <path d="M0,10 C150,60 300,75 420,65 C560,52 700,10 850,30 L850,100 L0,100Z" fill="#fff"/>
    <path d="M0,10 C150,60 300,75 420,65 C560,52 700,10 850,30 L850,40 C700,26 560,70 420,84 C300,94 150,78 0,18Z" fill="#000"/>
  </svg>

  <h2 class="abs display" style="left:102px;top:2100px;font-size:21px;line-height:28px">SUBSCRIBE OUR<br>NEWSLETTER</h2>
  <div class="field" style="left:389px;top:2114px;width:210px;height:29px;border-radius:15px;background:var(--field);font-size:8px;padding:10px 12px;color:#555">Enter Email Address</div>
  <div class="pill active" style="left:613px;top:2114px;width:136px;height:29px;line-height:26px;font-size:9px">Subscribe Now</div>
  <div class="rule" style="left:102px;top:2182px;width:647px"></div>
  <div class="abs brand" style="left:0;top:2222px;width:850px;justify-content:center;font-size:28px"><span class="dot" style="width:16px;height:16px"></span>Quorvane</div>
  <div class="abs center" style="left:0;top:2286px;width:850px;font-size:10.5px;font-weight:700">&#9993; hi@quorvane.nz</div>
  <div class="footnav" style="left:0;top:2312px;width:850px;font-size:8.5px;word-spacing:2px">HOME &nbsp;&nbsp;&nbsp;&nbsp;&nbsp;/&nbsp;&nbsp;&nbsp;&nbsp;&nbsp; WHAT WE DO &nbsp;&nbsp;&nbsp;&nbsp;&nbsp;/&nbsp;&nbsp;&nbsp;&nbsp;&nbsp; OUR PROJECTS &nbsp;&nbsp;&nbsp;&nbsp;&nbsp;/&nbsp;&nbsp;&nbsp;&nbsp;&nbsp; ABOUT US &nbsp;&nbsp;&nbsp;&nbsp;&nbsp;/&nbsp;&nbsp;&nbsp;&nbsp;&nbsp; CONTACT US</div>
  <div class="copy" style="left:0;top:2339px;width:850px;font-size:8px">Copyright© 2024 <u>Quorvane</u> | All Rights Reserved</div>
</section>

<!-- MOBILE -->
<section class="screen mobile">
  <div class="photo hero-photo" style="left:0;top:0;width:212px;height:290px" role="img" aria-label="Survey station on an alpine ridge above a braided river valley"></div>
  <div class="abs brand" style="left:12px;top:14px;font-size:11px;gap:4px"><span class="dot" style="width:7px;height:7px"></span>Quorvane</div>
  <svg class="abs" style="left:189px;top:18px" width="9" height="8" viewBox="0 0 9 8"><rect width="9" height="1.6" fill="#000"/><rect y="3.2" width="9" height="1.6" fill="#000"/><rect y="6.4" width="9" height="1.6" fill="#000"/></svg>
  <h1 class="abs display center" style="left:0;top:58px;width:212px;font-size:14px;line-height:20.5px;letter-spacing:1.5px">PRECISION.<br>EFFICIENCY.<br>CLARITY.</h1>
  <svg class="abs" style="left:0;top:262px" width="212" height="40" viewBox="0 0 212 40">
    <path d="M0,16 C40,28 80,30 110,26 C150,20 180,10 212,14 L212,40 L0,40Z" fill="#fff"/>
    <path d="M0,16 C40,28 80,30 110,26 C150,20 180,10 212,14 L212,18 C180,16 150,28 110,33 C80,36 40,33 0,19Z" fill="#000"/>
  </svg>
  <h2 class="abs display center" style="left:0;top:314px;width:212px;font-size:12px">WHAT WE DO</h2>
  <div class="pill active" style="left:29px;top:346px;width:155px;height:23px;line-height:20px;font-size:7px">Fieldwork Solutions</div>
  <div class="pill" style="left:29px;top:379px;width:155px;height:23px;line-height:20px;font-size:7px">Positioning and Monitoring</div>
  <div class="pill" style="left:29px;top:412px;width:155px;height:23px;line-height:20px;font-size:7px">Design and Prototyping</div>
  <div class="photo sea-photo" style="left:11px;top:465px;width:190px;height:158px;border-radius:4px" role="img" aria-label="Red inflatable boat bow heading across the sea toward a rocky coast"></div>
  <h3 class="abs" style="left:11px;top:647px;font-size:12px;font-weight:700;letter-spacing:.5px">FIELDWORK SOLUTIONS</h3>
  <ul class="service-list" style="left:11px;top:672px;font-size:7px">
    <li style="height:17.5px"><span class="mark" style="width:8px;height:5px;margin-right:9px"></span>Efficient product rollouts</li>
    <li style="height:17.5px"><span class="mark" style="width:8px;height:5px;margin-right:9px"></span>Equipment Installation &amp; Maintenance</li>
    <li style="height:17.5px"><span class="mark" style="width:8px;height:5px;margin-right:9px"></span>Surveying Techniques</li>
    <li style="height:17.5px"><span class="mark" style="width:8px;height:5px;margin-right:9px"></span>Precision GNSS instrumentation</li>
    <li style="height:17.5px"><span class="mark" style="width:8px;height:5px;margin-right:9px"></span>Seismic Instrumentation</li>
    <li style="height:17.5px"><span class="mark" style="width:8px;height:5px;margin-right:9px"></span>IOT Sensors</li>
    <li style="height:17.5px"><span class="mark" style="width:8px;height:5px;margin-right:9px"></span>Reliable Communications Systems</li>
    <li style="height:17.5px"><span class="mark" style="width:8px;height:5px;margin-right:9px"></span>Environmental sensors</li>
  </ul>
  <h2 class="abs display center" style="left:0;top:842px;width:212px;font-size:12px">CASE STUDIES</h2>
  <div class="photo hub" style="left:0;top:874px;width:10px;height:188px" role="img" aria-label="Edge of previous case study photo"></div>
  <div class="card dark" style="left:17px;top:874px;width:178px;height:188px;padding:0 10px">
    <div class="t" style="font-size:8.5px;line-height:12px;margin-bottom:9px">GNSS CORS station upgrade<br>and survey</div>
    <p style="font-size:6.5px;line-height:11.8px">Upgrade and reference mark survey of GNSS Continuously Operating Reference Stations (CORS) for the NZGA positioning network. This project enhanced the accuracy and reliability of the NZGA positioning network, crucial for a wide range of applications including land surveying, construction, and geospatial research.</p>
  </div>
  <div class="photo rail" style="left:202px;top:874px;width:10px;height:188px" role="img" aria-label="Edge of next case study photo"></div>
  <h2 class="abs display center" style="left:0;top:1095px;width:212px;font-size:12px">ABOUT US</h2>
  <div class="photo person" style="left:11px;top:1131px;width:170px;height:170px;border-radius:50%" role="img" aria-label="Team member in orange hi-vis on a mountain summit"></div>
  <div class="badge" style="left:131px;top:1226px;width:67px;height:67px;font-size:7px;line-height:11px"><b style="font-size:12px;line-height:15px">15+</b>Years of<br>Experience</div>
  <p class="para" style="left:11px;top:1323px;width:191px;font-size:7px;line-height:13.5px">Welcome to Quorvane, your reliable partner in delivering innovative solutions. Our team of skilled professionals is committed to excellence, ensuring every project is handled with precision, efficiency, and integrity.</p>
  <p class="para" style="left:11px;top:1387px;width:191px;font-size:7px;line-height:13.5px">We solve problems in the field, build robust infrastructure, and deliver accurate data to our clients. Let us help you achieve your goals with our tailored, sustainable solutions and exceptional service.</p>
  <div class="contact" style="top:1474px;width:212px;height:330px" role="img" aria-label="Dark mountain landscape at dusk"></div>
  <h2 class="abs display center" style="left:0;top:1502px;width:212px;font-size:12px;color:var(--white)">CONTACT US</h2>
  <div class="field" style="left:11px;top:1536px;width:190px;height:24px;font-size:6px;padding:8px 7px">Name</div>
  <div class="field" style="left:11px;top:1570px;width:190px;height:24px;font-size:6px;padding:8px 7px">Email Address</div>
  <div class="field" style="left:11px;top:1604px;width:190px;height:24px;font-size:6px;padding:8px 7px">Phone Number</div>
  <div class="field" style="left:11px;top:1638px;width:190px;height:48px;font-size:6px;padding:8px 7px">Message</div>
  <div class="ghost" style="left:38px;top:1711px;width:136px;height:28px;line-height:25px;font-size:7.5px">SUBMIT NOW</div>
  <svg class="abs" style="left:0;top:1774px" width="212" height="40" viewBox="0 0 212 40">
    <path d="M0,8 C40,20 80,22 110,18 C150,12 180,4 212,8 L212,40 L0,40Z" fill="#fff"/>
    <path d="M0,8 C40,20 80,22 110,18 C150,12 180,4 212,8 L212,12 C180,10 150,20 110,25 C80,28 40,25 0,11Z" fill="#000"/>
  </svg>
  <h2 class="abs display" style="left:11px;top:1834px;font-size:12px;line-height:16px">SUBSCRIBE OUR<br>NEWSLETTER</h2>
  <div class="field" style="left:11px;top:1880px;width:190px;height:25px;border-radius:13px;background:var(--field);font-size:7px;padding:8px 13px;color:#555">Enter Email Address</div>
  <div class="pill active" style="left:11px;top:1914px;width:114px;height:25px;line-height:22px;font-size:7px">Subscribe Now</div>
  <div class="rule" style="left:11px;top:1960px;width:190px"></div>
  <div class="abs brand" style="left:0;top:1986px;width:212px;justify-content:center;font-size:14px;gap:4px"><span class="dot" style="width:8px;height:8px"></span>Quorvane</div>
  <div class="abs center" style="left:0;top:2019px;width:212px;font-size:8px;font-weight:700">&#9993; hi@quorvane.nz</div>
  <div class="footnav" style="left:0;top:2039px;width:212px;font-size:6.5px;line-height:14px">HOME &nbsp;/&nbsp; WHAT WE DO &nbsp;/&nbsp; OUR PROJECTS &nbsp;/<br>ABOUT US &nbsp;/&nbsp; CONTACT US</div>
  <div class="copy" style="left:0;top:2071px;width:212px;font-size:6.5px">Copyright© 2024 <u>Quorvane</u> | All Rights Reserved</div>
</section>

</div>
</body>
</html>
```